Heronby Mortgage Capital Business Card

We need a business card design for our mortgage servicing company. In addition to servicing the loans of homeowners, we help homeowners with purchasing their homes and any mortgage refinancing. We would like to see designs that use the colors in the logo attached below (gold-ish yellow and navy blue), and any other design you deem fit! The design should communicate a simpler life with smart mortgages provided by Heronby.

```html
<!DOCTYPE html>
<html lang="en">
<head>
<meta charset="UTF-8">
<title>Heronby Mortgage Capital — Business Card</title>
<link href="https://fonts.googleapis.com/css2?family=Libre+Baskerville:wght@700&family=Montserrat:wght@400;500&display=swap" rel="stylesheet">
<style>
  :root {
    --backdrop: #232323;
    --navy: #262157;
    --gold: #e0b03c;
    --teal: #2aa3a3;
    --paper: #ffffff;
    --ink: #2b2a4a;
  }
  * { margin: 0; padding: 0; box-sizing: border-box; }
  html, body { width: 900px; height: 1200px; overflow: hidden; }
  body { background: var(--backdrop); position: relative; font-family: "Montserrat", sans-serif; }

  .card {
    position: absolute;
    left: 135px;
    width: 630px;
    height: 358px;
    border-radius: 12px;
    overflow: hidden;
  }
  .card--front { top: 214px; background: var(--navy); }
  .card--back { top: 629px; background: var(--paper); }

  .wordmark {
    font-family: "Libre Baskerville", serif;
    font-weight: 700;
    color: var(--gold);
    white-space: nowrap;
  }
  .card--front .wordmark {
    position: absolute;
    left: 0; right: 0; top: 148px;
    text-align: center;
    font-size: 52px;
    line-height: 1;
  }
  .card--back .wordmark {
    position: absolute;
    left: 40px; width: 270px; top: 166px;
    text-align: center;
    font-size: 24px;
    line-height: 1;
  }

  .divider {
    position: absolute;
    left: 344px; top: 95px;
    width: 2px; height: 170px;
    background: var(--teal);
  }

  .contact {
    position: absolute;
    left: 376px; top: 92px;
    color: var(--ink);
    font-size: 14.5px;
    letter-spacing: 0.04em;
  }
  .contact__name {
    font-family: "Libre Baskerville", serif;
    font-weight: 700;
    color: var(--gold);
    font-size: 21px;
    letter-spacing: 0;
    line-height: 1.2;
  }
  .contact__role { margin-top: 4px; font-size: 15px; }
  .contact__address { margin-top: 10px; line-height: 23px; }
  .contact__lines { margin-top: 9px; list-style: none; }
  .contact__lines li { display: flex; align-items: center; gap: 6px; height: 24px; }
  .contact__lines .phone { letter-spacing: 0.18em; }
  .contact__lines svg { width: 12px; height: 12px; fill: var(--gold); flex: none; }

  .swoosh { position: absolute; left: 0; bottom: 0; width: 630px; height: 358px; }
</style>
</head>
<body>
  <section class="card card--front" aria-label="Card front">
    <div class="wordmark">Heronby Mortgage</div>
  </section>

  <section class="card card--back" aria-label="Card back">
    <div class="wordmark">Heronby Mortgage</div>
    <div class="divider"></div>

    <div class="contact">
      <div class="contact__name">Dana Whitcombe</div>
      <div class="contact__role">Founder</div>
      <div class="contact__address">218 Harbor Row N<br>Bayfield, FL 34120</div>
      <ul class="contact__lines">
        <li>
          <svg viewBox="0 0 24 24" aria-hidden="true"><path d="M6.6 10.8a15.1 15.1 0 0 0 6.6 6.6l2.2-2.2a1 1 0 0 1 1-.25 11.4 11.4 0 0 0 3.6.57 1 1 0 0 1 1 1V20a1 1 0 0 1-1 1A17 17 0 0 1 3 4a1 1 0 0 1 1-1h3.5a1 1 0 0 1 1 1c0 1.25.2 2.45.57 3.6a1 1 0 0 1-.25 1z"/></svg>
          <span class="phone">(888)-410-2736</span>
        </li>
        <li>
          <svg viewBox="0 0 24 24" aria-hidden="true"><path d="M2 5h20v14H2z" fill="var(--gold)"/><path d="M2 6l10 7.5L22 6" fill="none" stroke="#fff" stroke-width="1.6"/></svg>
          <span>hello@heronbymtg.com</span>
        </li>
        <li>
          <svg viewBox="0 0 24 24" aria-hidden="true"><circle cx="12" cy="12" r="10" fill="none" stroke="var(--gold)" stroke-width="2"/><path d="M2 12h20M12 2c3 3 3 17 0 20M12 2c-3 3-3 17 0 20" fill="none" stroke="var(--gold)" stroke-width="1.6"/></svg>
          <span>www.heronbymtg.com</span>
        </li>
      </ul>
    </div>

    <svg class="swoosh" viewBox="0 0 630 358" aria-hidden="true">
      <path d="M255 358 Q420 326 630 327 L630 329.5 Q440 332 298 358 Z" fill="var(--gold)"/>
      <path d="M312 358 Q460 333 630 331 L630 358 Z" fill="var(--navy)"/>
    </svg>
  </section>
</body>
</html>
```